Maple Ridge business card design

Card needs to include the following text/items:
Company Logo
Tobin Marsh
Phone # - 555-318-7642
service@mapleridgelandscaping.example
Lawn & landscape maintenance services

```html
<!DOCTYPE html>
<html lang="en">
<head>
<meta charset="utf-8">
<title>Maple Ridge Landscaping – Business Card</title>
<link href="https://fonts.googleapis.com/css2?family=Crimson+Pro:wght@400;600&display=swap" rel="stylesheet">
<style>
  :root {
    --forest: #2e4d31;
    --olive: #7f9531;
    --ink: #333333;
    --paper: #ffffff;
    --cream: #f2f4ee;
    --stage-light: #fafafa;
    --stage-dark: #e2e2e2;
  }
  * { margin: 0; padding: 0; box-sizing: border-box; }
  html, body { width: 1200px; height: 594px; overflow: hidden; }
  body {
    position: relative;
    background: radial-gradient(ellipse at center, var(--stage-light) 0%, var(--stage-dark) 100%);
    font-family: "Crimson Pro", Georgia, serif;
  }
  .card {
    position: absolute;
    top: 141px;
    width: 442px;
    height: 295px;
    text-align: center;
  }
  .card--front { left: 139px; background: var(--paper); }
  .card--back { left: 619px; background: var(--forest); color: var(--cream); }

  .brand {
    position: absolute;
    left: 0; right: 0; top: 134px;
    display: flex;
    align-items: center;
    justify-content: center;
    gap: 10px;
  }
  .brand-dot {
    width: 18px; height: 18px;
    border-radius: 50%;
    background: var(--forest);
    flex: none;
  }
  .brand-name {
    color: var(--forest);
    font-weight: 600;
    font-size: 22px;
    line-height: 26px;
  }
  .tagline {
    position: absolute;
    left: 105px; width: 232px; top: 242px;
    color: var(--ink);
    font-size: 13.5px;
    line-height: 18px;
    border-bottom: 2px solid var(--olive);
    padding-bottom: 1px;
  }

  .contact-name, .contact-phone {
    position: absolute;
    left: 0; right: 0;
    font-size: 16px;
    line-height: 18px;
  }
  .contact-name { top: 129px; }
  .contact-phone { top: 148px; }
  .contact-rule {
    position: absolute;
    left: 148px; width: 146px; top: 168px;
    border-top: 2px solid var(--olive);
  }
  .contact-email {
    position: absolute;
    left: 0; right: 0; top: 246px;
    font-size: 13.5px;
    line-height: 18px;
  }

  .side-label {
    position: absolute;
    top: 468px;
    width: 442px;
    text-align: center;
    color: var(--ink);
    font-size: 13.5px;
    letter-spacing: 0.3px;
  }
  .side-label--front { left: 139px; }
  .side-label--back { left: 619px; }
</style>
</head>
<body>
  <section class="card card--front">
    <div class="brand">
      <span class="brand-dot" aria-hidden="true"></span>
      <span class="brand-name">Maple Ridge Landscaping</span>
    </div>
    <p class="tagline">Lawn &amp; Landscape Maintenance Services</p>
  </section>

  <section class="card card--back">
    <p class="contact-name">Tobin Marsh</p>
    <p class="contact-phone">Phone# 555-318-7642</p>
    <div class="contact-rule"></div>
    <p class="contact-email">service@mapleridgelandscaping.example</p>
  </section>

  <p class="side-label side-label--front">FRONT</p>
  <p class="side-label side-label--back">BACK</p>
</body>
</html>
```